Verostel business card

Business card for sustainable investment company called "Verostel". Verostel is an exchange platform selling carbon credits between buyers and sellers. Carbon Credits are an environmental commodity for reducing global carbon emissions.

the card should obviously have our logo and the theme should be sustainability/environment mixed with a trading platform.

Contact Information for Business Card

Logo, Name, Title, Phone, Email

Colors
0054AA
0677BA
7BADD7
CADEEF
E8F1F8
0094D4
00A9DD
6FCCEA
C7EBF8
E9F6FB
00AB8E
00BBA5
67D7C9
C6EFE9
E9F9F6
59FF00
82FF00
B8FF75
E3FFCB
F4FFEA

```html
<!DOCTYPE html>
<html lang="en">
<head>
<meta charset="utf-8">
<title>Verostel business card</title>
<link rel="stylesheet" href="https://fonts.googleapis.com/css2?family=Montserrat:wght@700;800&family=Lato:wght@300;400&display=swap">
<style>
  :root {
    --page: #d9d9d9;
    --card: #1a1a1b;
    --card-back: #1c1c1d;
    --white: #ffffff;
    --cyan: #4fc6e0;
    --sky: #2fc3ef;
    --blue: #4a86c8;
    --gloss: #2e2e30;
  }
  * { box-sizing: border-box; margin: 0; padding: 0; }
  html, body { width: 1200px; height: 856px; overflow: hidden; }
  body {
    background: var(--page);
    position: relative;
    font-family: "Lato", sans-serif;
  }
  .card {
    position: absolute;
    top: 268px;
    width: 560px;
    height: 320px;
    overflow: hidden;
    border-radius: 3px;
    box-shadow: 0 6px 18px rgba(0,0,0,.25);
  }
  .card-front { left: 30px; background: var(--card); }
  .card-back { left: 610px; background: var(--card-back); }

  .brand {
    position: absolute;
    left: 34px;
    top: 36px;
    display: flex;
    align-items: center;
    gap: 12px;
  }
  .brand-square {
    width: 16px;
    height: 16px;
    background: var(--sky);
  }
  .brand-name {
    font-family: "Montserrat", sans-serif;
    font-weight: 800;
    font-size: 38px;
    letter-spacing: -0.5px;
    color: var(--white);
    line-height: 1;
  }

  .person {
    position: absolute;
    right: 40px;
    top: 40px;
    text-align: right;
  }
  .person-name {
    font-family: "Montserrat", sans-serif;
    font-weight: 700;
    font-size: 19px;
    color: var(--cyan);
    letter-spacing: 0.3px;
  }
  .person-title {
    font-family: "Lato", sans-serif;
    font-weight: 300;
    font-size: 14px;
    color: var(--white);
    margin-top: 3px;
  }
  .accent-bar {
    position: absolute;
    right: 0;
    top: 40px;
    width: 14px;
    height: 42px;
    background: var(--cyan);
  }

  .contacts {
    position: absolute;
    left: 34px;
    top: 118px;
    list-style: none;
  }
  .contacts li {
    display: flex;
    align-items: center;
    gap: 8px;
    font-size: 14px;
    font-weight: 300;
    color: var(--white);
    line-height: 23px;
  }
  .contacts svg { width: 11px; height: 11px; flex: none; }
  .address {
    position: absolute;
    left: 34px;
    top: 206px;
    font-size: 14px;
    font-weight: 300;
    color: var(--white);
    line-height: 22px;
  }

  .decor {
    position: absolute;
    left: 300px;
    top: 128px;
    width: 250px;
    height: 230px;
    border-radius: 14px;
    background: linear-gradient(160deg, var(--cyan) 0%, var(--sky) 45%, var(--blue) 100%);
  }

  .back-name {
    position: absolute;
    left: 0;
    right: 0;
    top: 130px;
    text-align: center;
    font-family: "Montserrat", sans-serif;
    font-weight: 800;
    font-size: 54px;
    letter-spacing: -0.5px;
    color: var(--gloss);
    line-height: 1;
  }
</style>
</head>
<body>

  <section class="card card-front">
    <div class="brand">
      <span class="brand-square"></span>
      <span class="brand-name">VEROSTEL</span>
    </div>

    <div class="person">
      <div class="person-name">DANIEL HARLOW</div>
      <div class="person-title">Managing Director</div>
    </div>
    <span class="accent-bar"></span>

    <ul class="contacts">
      <li>
        <svg viewBox="0 0 12 12"><path fill="#4fc6e0" d="M2.4 1h2l1 2.6-1.3.9a6.5 6.5 0 0 0 3.4 3.4l.9-1.3 2.6 1v2A1.4 1.4 0 0 1 9.6 11 8.6 8.6 0 0 1 1 2.4 1.4 1.4 0 0 1 2.4 1z"/></svg>
        123 456 789
      </li>
      <li>
        <svg viewBox="0 0 12 12"><rect x="0.5" y="2" width="11" height="8" rx="1" fill="#4fc6e0"/><path d="M1 2.6l5 3.8 5-3.8" fill="none" stroke="#1a1a1b" stroke-width="1"/></svg>
        info@verostel.com
      </li>
      <li>
        <svg viewBox="0 0 12 12"><circle cx="6" cy="6" r="5.3" fill="none" stroke="#4fc6e0" stroke-width="1.2"/><ellipse cx="6" cy="6" rx="2.3" ry="5.3" fill="none" stroke="#4fc6e0" stroke-width="1"/><path d="M0.8 6h10.4" stroke="#4fc6e0" stroke-width="1"/></svg>
        www.verostel.com
      </li>
    </ul>

    <p class="address">Your address, City<br>State, Zip 1234</p>

    <div class="decor" role="img" aria-label="Large brand decoration in cyan to blue gradient"></div>
  </section>

  <section class="card card-back">
    <div class="back-name">VEROSTEL</div>
  </section>

</body>
</html>
```